Grins Circle Brochure highlighting office, club membership, dentist to attract new members

This brochure is for prospective patients who are interested in joining our Exclusive Member Only program. The brochure should explain the exclusivity of the club, club fees, membership benefits, office hightlights, friendly staff, experienced Dentist, Also can refer to our website www.dentistkavra.example for more information to go into brochure.

Our mission is to provide a quality care your smile needs, comfort & luxury you deserve.

Staff - Our dedicated, friendly & experience staff are well equipped to answer all your questions and make every visit as memorable as the previous the one. We believe Care for your comfort is as important as Care your Smile needs. We strive to make every aspect of your visit as smooth and effortless as possible.

Dentist - Dr. Kavra, I have extensive experience in general, cosmetic & orthodontic treatments. I continue to attend continued education more than required by the dental association. My only motivation is to bring the best of the procedures and technology available in the market today for my patients. I am also a member of many professional organizations in DC metro area which helps share and promote best practices in the industry. Outside of Dentistry I love to spend time with my 6 and 2 yr olds as a nature lover I get to hike regularly, as weather gets cold, I love to hit the thread mil with my fav music. Yoga stretches are part of my in between procedures.

Office - Our office has been in the current location for over 30 years. Our office has been updated continuously, however we continue to keep the warm and relaxing ambience. The reception area is the hallmark of our core principle. The coffee station with the traditional seating helps us set the warm and cozy tone for the rest of the office. The water fountain adds the relaxing experience. Though many patients have noted they don’t get to enjoy the reception area as they don’t usually get to wait. We take that as a compliment.

Operatory
We have three operatories Meadow, Lanternwood & Bluebrook each named to reflect the essence we strive for in all aspect of our practice. Each operatory is equipped with varied softrelmic firmness for your comfort. All the operatories are kept clean and well organized for visual and functional smoothness. The technologies are kept upto date to ensure our services are unparalleled. We offer warm cotton towels during long procedures to ensure comfortness. We make individual eye shades to protect the eyes.

Restroom
Last but not the least we are proud of our restroom, we ensure our standards and attention to the details are carried through and through. Cotton towels are available to help freshen up after a long procedure.

The Club
I know you have been waiting to know about the club. I saved the best to the last. Grins Circle is the crown jewel of our practice. As part of my quest to continue to improve our services, after a considerable thought and iterations we conceived this program. The core objective is to bring another level of comfort to our patients. The program brings all the aspects of our being together in a simple package. Instead of breaking the essentials like cleaning, Xrays, Fluoride, whitening, diagnosis, consultation,emergency visits,, we simplified everything into one simple club membership. As a member of Grins Circle you will get all of the basic essentials included in your program. Also you will receive membership discounts from 15% to 25% in all the procedures. The best part of the program is all your procedures cost can be financed at 0% interest. As always our staff stay on top of your essential treatments, reaching out to you by your preferred mode of contact and ensure you get your essentials done at your convenience.

Pricing

The Grins Circle program is a subscription program. Patients pay monthly subscription. This simple monthly subscription covers all the essential routine dental care including Cleaning, XRays, Fluoride treatment, Whitening, Diagnosis, Consultation, Emergency visits.

Single membership is $59 a month
Family of Two membership is $49 per person per month
Family of Three and more is $39 per person per month

Members receive 15% to 25% discounts on all of the below procedures

Orthodontic - Clearvane, Braces
Implants
Bridges
Crowns
Tooth Extractions
Rylaxo treatments
Laser Gum Treatments
Veneers, Bonding
Fillings
Dentures

Target Market(s)

high income group, family, professionals, teens

Industry/Entity Type

Club

Font styles to use
Script

Colors
3176b5

Requirements
Must have
• Logo, pic of Dentist, office pics

```html
<!DOCTYPE html>
<html lang="en">
<head>
<meta charset="utf-8">
<title>Grins Circle Brochure</title>
<link rel="stylesheet" href="https://fonts.googleapis.com/css2?family=Great+Vibes&family=Open+Sans:ital,wght@0,400;0,600;0,700;0,800;1,700&display=swap">
<style>
  :root {
    --brand-blue: #3176b5;
    --ink: #1d1d1f;
    --band-black: #222224;
    --band-grey: #b9bbbe;
    --paper: #ffffff;
    --backdrop: #3a3b3d;
    --badge-green: #2e8a3e;
    --text-dark: #111;
  }
  * { box-sizing: border-box; margin: 0; padding: 0; }
  html, body { width: 1200px; height: 776px; overflow: hidden; }
  body {
    background: var(--backdrop);
    font-family: "Open Sans", Arial, sans-serif;
    position: relative;
  }
  .page {
    position: absolute;
    top: 23px;
    width: 540px;
    height: 730px;
    background: var(--paper);
    overflow: hidden;
    box-shadow: 0 8px 24px rgba(0,0,0,.45);
  }
  .page--front { left: 30px; }
  .page--back { left: 630px; }

  .masthead { position: absolute; left: 0; top: 0; width: 540px; height: 95px; }
  .masthead svg { position: absolute; inset: 0; }
  .masthead__title {
    position: absolute; left: 0; right: 0; top: 4px;
    text-align: center;
    font-family: "Great Vibes", cursive;
    color: #fff; font-size: 58px; line-height: 70px;
    word-spacing: 14px;
  }

  .photo { position: absolute; }
  .photo--dentist { left: 0; top: 82px; width: 298px; height: 262px; background: linear-gradient(160deg, #e9eef3, #a9c6e2 70%, #7fa9d4); }
  .photo--office-1 { left: 304px; top: 78px; width: 236px; height: 80px; background: linear-gradient(180deg, #d8d6d2, #6f7377); }
  .photo--office-2 { left: 304px; top: 162px; width: 236px; height: 86px; background: linear-gradient(120deg, #7a4d3a, #e6e3df 45%, #2b2d3a); }
  .photo--office-3 { left: 304px; top: 252px; width: 236px; height: 92px; background: linear-gradient(150deg, #e8dcc8, #8a5c3c 60%, #5a3a28); }

  .ribbon {
    position: absolute; left: 0; top: 332px; width: 540px; height: 30px;
    background: var(--brand-blue); color: #fff;
    font-weight: 700; font-style: italic; font-size: 15px;
    line-height: 30px; text-align: center;
  }
  .band { position: absolute; left: 0; width: 540px; color: #fff; font-weight: 700; padding: 0 20px; }
  .band--lead { top: 362px; height: 40px; background: var(--band-black); font-size: 18.5px; line-height: 40px; }
  .band--covers { top: 402px; height: 58px; background: var(--brand-blue); font-size: 17px; line-height: 24px; padding-top: 5px; }
  .band--essentials { top: 460px; height: 26px; background: var(--band-grey); color: var(--ink); font-size: 11.5px; line-height: 26px; font-weight: 600; }

  .price-tab {
    position: absolute; left: 0; width: 220px; color: #fff;
    border-radius: 0 12px 12px 0; padding: 7px 14px;
    font-weight: 700; font-size: 14px; line-height: 18px;
  }
  .price-tab--blue { background: var(--brand-blue); }
  .price-tab--black { background: var(--band-black); }
  .price-tab strong { font-size: 27px; font-weight: 800; }
  .price-tab--single { top: 500px; height: 66px; }
  .price-tab--two { top: 570px; height: 72px; }
  .price-tab--three { top: 646px; height: 72px; }

  .discounts { position: absolute; left: 236px; top: 498px; width: 300px; }
  .discounts__intro { font-weight: 700; font-size: 14px; line-height: 19px; color: var(--text-dark); }
  .procedures { display: flex; gap: 18px; margin-top: 8px; }
  .procedures ul { list-style: none; }
  .procedures li {
    color: var(--brand-blue); font-weight: 600; font-size: 14px; line-height: 24px;
    padding-left: 16px; position: relative;
  }
  .procedures li::before {
    content: ""; position: absolute; left: 0; top: 9px; width: 6px; height: 6px; background: var(--text-dark);
  }
  .badge { position: absolute; left: 450px; top: 640px; width: 56px; height: 56px; border-radius: 50%; background: var(--badge-green); }

  .band--staff {
    top: 70px; height: 62px; background: var(--band-black);
    font-size: 9px; line-height: 12px; font-weight: 400; padding: 14px 22px 0;
  }
  .label { color: var(--brand-blue); font-weight: 700; font-size: 11px; }
  .photo--team { left: 22px; top: 132px; width: 496px; height: 160px; background: linear-gradient(180deg, #cbb89c, #8a6e55 40%, #4f95b5 80%, #3a7ca0); }
  .dentist-bio { position: absolute; left: 22px; top: 296px; width: 496px; font-size: 9.2px; line-height: 12.5px; color: var(--text-dark); text-align: justify; }

  .club { position: absolute; left: 0; top: 392px; width: 540px; height: 172px; background: var(--band-black); padding: 16px 34px 0; }
  .club__title { color: var(--brand-blue); text-align: center; font-weight: 700; font-size: 26px; line-height: 32px; }
  .club__text { color: #fff; font-size: 14.2px; line-height: 24px; text-align: center; margin-top: 4px; }

  .location { position: absolute; top: 580px; font-size: 11px; line-height: 15px; color: var(--text-dark); }
  .location--north { left: 24px; }
  .location--east { left: 196px; }
  .location__name { color: var(--brand-blue); font-weight: 700; font-size: 11.5px; }
  .location__phone { margin-top: 6px; }
  .location__phone b { color: var(--brand-blue); font-size: 14px; }
  .map { position: absolute; left: 392px; top: 566px; width: 132px; height: 100px; border-radius: 50%; background: radial-gradient(circle, #f3efe6, #dfe7d8 70%, #cfd8cc); }
  .web { position: absolute; left: 24px; top: 678px; color: var(--brand-blue); font-weight: 800; font-size: 29px; line-height: 36px; }
</style>
</head>
<body>

<section class="page page--front">
  <header class="masthead">
    <svg width="540" height="95" viewBox="0 0 540 95" aria-hidden="true">
      <path d="M0 0H540V58Q300 62 0 92Z" fill="#3176b5"/>
    </svg>
    <h1 class="masthead__title">Grins Circle</h1>
  </header>

  <div class="photo photo--dentist" role="img" aria-label="Portrait of Dr. Kavra in blue scrubs"></div>
  <div class="photo photo--office-1" role="img" aria-label="Operatory with dental chair"></div>
  <div class="photo photo--office-2" role="img" aria-label="Dental chair beside framed artwork"></div>
  <div class="photo photo--office-3" role="img" aria-label="Warm reception area"></div>

  <p class="ribbon">Quality Care Your Smile Needs, Comfort &amp; Luxury You Deserve</p>
  <p class="band band--lead">The Grins Circle program is a subscription program</p>
  <p class="band band--covers">Patients pay monthly subscription. This simple monthly subscription covers all the essential routine dental care</p>
  <p class="band band--essentials">Cleaning, XRays, Fluoride treatment, Whitening, Diagnosis, Consultation, Emergency Visits</p>

  <div class="price-tab price-tab--blue price-tab--single">Single membership<br>is <strong>$59</strong> a month</div>
  <div class="price-tab price-tab--black price-tab--two">Family of Two<br>membership is <strong>$49</strong><br>per person per month</div>
  <div class="price-tab price-tab--blue price-tab--three">Family of Three<br>&amp; more is <strong>$39</strong><br>per person per month</div>

  <div class="discounts">
    <p class="discounts__intro">Members receive 15% to 25% discounts on all of the below procedures:</p>
    <div class="procedures">
      <ul>
        <li>Orthodontic</li><li>Clearvane</li><li>Braces</li><li>Implants</li><li>Bridges</li><li>Crowns</li>
      </ul>
      <ul>
        <li>Tooth Extractions</li><li>Rylaxo treatments</li><li>Laser Gum Treatments</li><li>Veneers, Bonding</li><li>Fillings</li><li>Dentures</li>
      </ul>
    </div>
  </div>
  <div class="badge" role="img" aria-label="Professional association badge"></div>
</section>

<section class="page page--back">
  <header class="masthead">
    <svg width="540" height="95" viewBox="0 0 540 95" aria-hidden="true">
      <path d="M0 0H540V58Q300 62 0 92Z" fill="#3176b5"/>
    </svg>
    <h1 class="masthead__title">Grins Circle</h1>
  </header>

  <p class="band band--staff"><span class="label">Staff</span> - Our dedicated, friendly &amp; experience staff are well equipped to answer all your questions and make every visit as memorable as the previous the one. We believe Care for your comfort is as important as Care your needs. We strive to make every aspect of your visit as smooth and effortless as possible.</p>

  <div class="photo photo--team" role="img" aria-label="Dr. Kavra with the friendly office staff"></div>

  <p class="dentist-bio"><span class="label">Dentist</span> - Dr. Kavra, I have extensive experience in general, cosmetic &amp; orthodontic treatments. I continue to attend continued education more than required by the dental association. My only motivation is to bring the best of the procedures and technology available in the market today for my patients. I am also a member of many professional organizations in DC metro area which helps share and promote best practices in the industry. Outside of Dentistry I love to spend time with my 6 and 2 yr olds as a nature lover I get to hike regularly, as weather gets cold, I love to hit the thread mil with my fav music. Yoga stretches are part of my in between procedures.</p>

  <section class="club">
    <h2 class="club__title">The Club</h2>
    <p class="club__text">I know you have been waiting to know about the club. I saved the best to the last. Grins Circle is the crown jewel of our practice. As part of my quest to continue to improve our services, after a considerable thought and iterations we conceived this program. The core objective is to bring another level of comfort to our patients.</p>
  </section>

  <address class="location location--north">
    <div class="location__name">Grins Circle of Northfield</div>
    1820 Larkspur Ave, Suite 114<br>Northfield, MD, United States<br>20000
    <div class="location__phone">Call us @ <b>301-555-0142</b></div>
  </address>
  <address class="location location--east">
    <div class="location__name">Grins Circle of Eastbrook</div>
    3390 Willowmere Rd, Suite 212<br>Eastbrook, MD, United States<br>20001
    <div class="location__phone">Call us @ <b>301-555-0187</b></div>
  </address>
  <div class="map" role="img" aria-label="Map showing the office locations"></div>
  <p class="web">www.dentistkavra.example</p>
</section>

</body>
</html>
```